Larkfield Advisory Group LLC Business Card Design

I'm looking for a fresh, sharp, clean and current/modern format for my company. This is a start up in the professional services (security/risk management consulting) industry. Catering to C-suite executives as well as senior director types of halcyon 800 companies.

Target Market(s)

Halcyon 800 companies and their C-suite staff with particular focus on VP of Human Resources and Director of Security.

Industry/Entity Type

Business

Font styles to use
Serif

Colors
0455a3
9bcb3c
acd037
3377b5
eaf1f7

Requirements
Must have
• Fresh, sharp, clean and current/modern look and feel.

```html
<!DOCTYPE html>
<html lang="en">
<head>
<meta charset="utf-8">
<title>Larkfield Advisory Group – Business Card</title>
<link rel="stylesheet" href="https://fonts.googleapis.com/css2?family=Fira+Sans+Condensed:wght@600&display=swap">
<style>
  :root {
    --navy: #1f2a5c;
    --green: #72a83f;
    --white: #ffffff;
    --backdrop: #ececec;
  }
  * { margin: 0; padding: 0; box-sizing: border-box; }
  html, body {
    width: 1200px;
    height: 1000px;
    overflow: hidden;
    background: var(--backdrop);
  }
  .business-card {
    position: absolute;
    left: 322px;
    top: 318px;
    width: 586px;
    height: 315px;
  }
  .card-artwork {
    position: absolute;
    inset: 0;
    width: 586px;
    height: 315px;
    display: block;
  }
  .brand-lockup {
    position: absolute;
    left: 160px;
    top: 124px;
    display: flex;
    align-items: center;
    gap: 30px;
  }
  .brand-dot {
    width: 70px;
    height: 70px;
    border-radius: 50%;
    background: var(--navy);
    flex: none;
  }
  .brand-text {
    display: flex;
    flex-direction: column;
    align-items: stretch;
  }
  .brand-name {
    font-family: "Fira Sans Condensed", sans-serif;
    font-weight: 600;
    color: var(--navy);
    font-size: 42px;
    line-height: 0.95;
    letter-spacing: 0.5px;
    text-transform: uppercase;
    white-space: nowrap;
  }
  .brand-subname {
    margin-top: 3px;
    font-family: "Fira Sans Condensed", sans-serif;
    font-weight: 600;
    color: var(--navy);
    font-size: 16px;
    line-height: 1;
    letter-spacing: 2.6px;
    text-transform: uppercase;
    white-space: nowrap;
  }
  .brand-tagline {
    margin-top: 7px;
    display: flex;
    align-items: center;
    gap: 5px;
    font-family: "Fira Sans Condensed", sans-serif;
    font-weight: 600;
    color: var(--green);
    font-size: 11px;
    line-height: 1;
    letter-spacing: 1px;
    text-transform: uppercase;
    white-space: nowrap;
  }
  .brand-tagline::before,
  .brand-tagline::after {
    content: "";
    flex: 1;
    height: 1px;
    background: var(--green);
  }
</style>
</head>
<body>
  <div class="business-card">
    <svg class="card-artwork" viewBox="0 0 586 315" aria-hidden="true">
      <rect class="card-base" width="586" height="315" fill="var(--navy)"/>
      <path class="green-band" fill="var(--green)"
            d="M28,0 L558,0 Q600,160 488,315 L96,315 Q-10,160 28,0 Z"/>
      <path class="top-arc" fill="var(--navy)"
            d="M108,0 L478,0 Q496,30 508,64 Q293,30 78,64 Q90,30 108,0 Z"/>
      <path class="content-panel" fill="var(--white)"
            d="M78,64 Q293,30 508,64 Q540,158 514,252 Q293,290 65,250 Q45,158 78,64 Z"/>
    </svg>
    <div class="brand-lockup">
      <span class="brand-dot"></span>
      <div class="brand-text">
        <span class="brand-name">Larkfield</span>
        <span class="brand-subname">Advisory Group</span>
        <span class="brand-tagline">Clear, Calm &amp; Sure</span>
      </div>
    </div>
  </div>
</body>
</html>
```